Gil’s NY Pizza Menu & Logo design

Looking for something that I can put on an 8.5x14 and also larger for an in-house menu to laminate. This is for a pizzeria, it doesn’t need to have that logo on it, I need a new design that is clean and I can use for shirts and signs. Want something modern and clean. This pizzeria is established and we are looking to rebrand. I have the current logo on the menu submission.

Target Market(s)

Looking for a new logo and menu design for my Pizzeria.

Industry/Entity Type

restaurant

Font styles to use
Sans Serif

Requirements
Must have
• Clean and fresh design for the logo that works for the menu, shirts, and signs.
Nice to have
• Open to any design, I want something completely catchy and updated.

```html
<!DOCTYPE html>
<html lang="en">
<head>
<meta charset="utf-8">
<title>Gil’s NY Pizza Menu</title>
<link href="https://fonts.googleapis.com/css2?family=Open+Sans:wght@400;600;700;800&display=swap" rel="stylesheet">
<style>
:root{
  --red:#e4332a;
  --black:#141414;
  --ink:#ffffff;
  --gold:#e9b23a;
  --bg:#e4e4e4;
  --leader:rgba(255,255,255,.55);
}
*{box-sizing:border-box;margin:0;padding:0}
html,body{width:1200px;height:1200px;overflow:hidden;background:var(--bg);font-family:"Open Sans",Arial,sans-serif;color:var(--ink)}
.spread{position:absolute;left:138px;width:924px;height:560px;display:flex}
.spread--outside{top:20px}
.spread--inside{top:620px}
.panel{position:relative;width:308px;height:100%;overflow:hidden;padding:20px 22px;font-size:6.4px;line-height:1.28}
.panel--red{background:var(--red)}
.panel--black{background:var(--black)}
.panel--split{padding:0}
.panel--split .top{background:var(--red);padding:20px 22px;height:200px}
.panel--split .bottom{background:var(--black);padding:10px 22px;height:360px}
h2{font-size:8.4px;font-weight:800;text-transform:uppercase;margin:0 0 6px;letter-spacing:.2px}
h2.accent{color:var(--red)}
h2.mixed{text-transform:none;font-size:9px}
.section{margin-bottom:14px}
.item{margin-bottom:6px}
.row{display:flex;align-items:flex-end}
.row .lead{flex:1;border-bottom:1px dotted var(--leader);margin:0 2px 2px}
.sub{opacity:.95}
.sizes .row{margin-left:150px}
.photo{position:absolute;left:0;right:0}
.brand{position:absolute;top:20px;left:50%;transform:translateX(-50%);display:flex;align-items:center;gap:8px;white-space:nowrap}
.brand .dot{width:16px;height:16px;border-radius:50%;background:var(--gold)}
.brand .name{font-size:22px;font-weight:800;color:var(--ink)}
.center-title{position:absolute;top:200px;left:0;right:0;text-align:center}
.center-title h1{color:var(--red);font-size:17px;font-weight:800;letter-spacing:.3px}
.center-title p{font-size:6.4px;line-height:1.3}
.over{position:absolute;left:14px;right:150px}
</style>
</head>
<body>

<!-- Outside spread -->
<section class="spread spread--outside">
  <div class="panel panel--red">
    <div class="section">
      <h2>Lunch Specials</h2>
      <div class="item"><div class="row">2 Slices of Pizza &amp; 20 oz Drink<span class="lead"></span>$8.99</div><div class="sub">Choose your drink. Add a slice topping if you’d like</div></div>
      <div class="item"><div class="row">Slice of Pizza &amp; Small Salad &amp; 20 oz Drink<span class="lead"></span>$9.99</div><div class="sub">Choice of dressing and drink.</div></div>
      <div class="item"><div class="row">Slice of Pizza &amp; 6 Wings &amp; 20 oz Drink<span class="lead"></span>$12.99</div><div class="sub">Choose wing sauce and your drink</div></div>
      <div class="item"><div class="row">Any Philly Cheesesteak &amp; 20 oz Drink<span class="lead"></span>$10.99</div><div class="sub">Choose your drink. Philly add-ons available</div></div>
    </div>
    <div class="section">
      <h2>Daily Specials</h2>
      <div class="item"><div class="row">Medium Cheese Pizza &amp; 10 Wings<span class="lead"></span>$29.95</div><div class="sub">Choose wing style and sauce.</div></div>
      <div class="item"><div class="row">Large 16" Cheese Pizza &amp; 20 Wings<span class="lead"></span>$39.95</div><div class="sub">Choose wing style and sauce, then add pizza toppings if you’d like.</div></div>
      <div class="item"><div class="row">2 Large 16" Pizzas<span class="lead"></span>$30.99</div><div class="sub">Add toppings to either pie.</div></div>
      <div class="item"><div class="row">18" Cheese Pizza, 24 Wings &amp; 2 Liter Soda<span class="lead"></span>$45.99</div><div class="sub">Choose wing style, sauce, soda, and pizza toppings</div></div>
    </div>
    <div class="section">
      <h2>Calzones</h2>
      <div class="item"><div class="row">Traditional Calzone<span class="lead"></span>$11.99</div><div class="sub">Mozzarella &amp; Ricotta Cheese</div></div>
      <div class="item"><div class="row">NY Supreme Calzone<span class="lead"></span>$14.99</div><div class="sub">Pepperoni, Sausage, Mushrooms, Onions,<br>Green Peppers, Mozzarella, &amp; Ricotta Cheese</div></div>
      <div class="item"><div class="row">Veggie Calzone<span class="lead"></span>$12.99</div><div class="sub">Black Olives, Mushrooms, Onions, Green Peppers,<br>Mozzarella, &amp; Ricotta Cheese</div></div>
      <div class="item" style="margin-top:14px"><div class="row">Meat Lovers Calzone<span class="lead"></span>$14.99</div><div class="sub">Sausage, Pepperoni, Ham, Bacon, Mozzarella, &amp; Ricotta Cheese</div></div>
      <h2 class="mixed" style="margin:8px 0 2px">Extra calzone toppings:</h2>
      <div class="sub">$.75 each: Anchovies • Banana Peppers • Black Olives • Green Olives • Extra Cheese • Extra Sauce • Garlic • Green Peppers • Ham • Jalapeños • Meatballs • Mushrooms • Onions • Pepperoni • Pineapple • Salami • Sausage • Spinach • Tomatoes • Bacon • Broccoli<br>$1.00 each: Artichokes • Bacon • Chicken • Eggplant • Green Olives • Meatball • Ricotta</div>
    </div>
  </div>

  <div class="panel panel--black">
    <svg class="photo" style="top:150px;height:410px" width="308" height="410" role="img" aria-label="Photo of a baked calzone cut open on a wooden board">
      <defs>
        <radialGradient id="calzoneGlow" cx="55%" cy="60%" r="60%">
          <stop offset="0" stop-color="#8a7a66"/>
          <stop offset=".55" stop-color="#3d342c"/>
          <stop offset="1" stop-color="#141414"/>
        </radialGradient>
      </defs>
      <rect width="308" height="410" fill="url(#calzoneGlow)"/>
    </svg>
    <div class="brand"><span class="dot"></span><span class="name">Gil’s NY Pizza</span></div>
    <div class="center-title" style="top:64px"><p style="font-size:7px;font-weight:700">STONE COOKED PIZZA<br>WINGS • CHEESESTEAKS</p></div>
    <div class="center-title">
      <h1>GIL’S NY PIZZA</h1>
      <p>STONE COOKED PIZZA<br>WINGS • CHEESESTEAKS • CALZONES<br>OWNER’S FAVORITE<br>The Gil’s Chicken &amp; Jalapeño<br>Built for Gil himself.</p>
    </div>
    <div class="over" style="top:330px;right:120px">
      <h2 class="accent">Drinks</h2>
      <div class="item"><div class="row">20 oz Soda<span class="lead"></span>$1.99</div><div class="sub">Doc Spark, Pop Cola, Sunny Lime, Orange Soda, Diet Pop Cola</div></div>
      <div class="item"><div class="row">2 Liter Soda<span class="lead"></span>$2.99</div><div class="sub">Doc Spark, Pop Cola, Sunny Lime, Orange Soda, Diet Pop Cola</div></div>
      <h2 class="accent" style="margin-top:12px">Desserts</h2>
      <div class="item"><div class="row">Cheesecake<span class="lead"></span>$4.99</div></div>
      <div class="item"><div class="row">Tiramisu<span class="lead"></span>$5.50</div></div>
      <div class="item"><div class="row">Cannoli<span class="lead"></span>$4.99</div></div>
    </div>
  </div>

  <div class="panel panel--split">
    <div class="top">
      <h2>Pizza Rolls</h2>
      <div class="item"><div class="row">Cheese Pizza Roll<span class="lead"></span>$11.49</div></div>
      <div class="item"><div class="row">Pepperoni Pizza Roll<span class="lead"></span>$12.99</div><div class="sub">Pepperoni &amp; Cheese</div></div>
      <div class="item"><div class="row">Meat Lovers Pizza Roll<span class="lead"></span>$13.99</div><div class="sub">Pepperoni, Sausage, Ham, Bacon, &amp; Cheese</div></div>
      <div class="item"><div class="row">Veggie Pizza Roll<span class="lead"></span>$13.99</div><div class="sub">Mushrooms, Green Peppers, Onions, Black Olives, &amp; Cheese</div></div>
      <div class="item"><div class="row">Supreme Pizza Roll<span class="lead"></span>$13.99</div><div class="sub">Pepperoni, Sausage, Mushroom, Green Peppers, Onions, &amp; Cheese</div></div>
      <div class="item"><div class="row">Buffalo Chicken Pizza Roll<span class="lead"></span>$13.99</div><div class="sub">Buffalo Chicken &amp; Cheese</div></div>
      <div class="item"><div class="row">Chicken, Bacon, Jalapeños &amp; Ranch Pizza Roll<span class="lead"></span>$13.99</div><div class="sub">It is what it says, Plus Cheese</div></div>
    </div>
    <div class="bottom">
      <h2 class="accent">Salads</h2>
      <div class="item"><div class="row">Garden Salad<span class="lead"></span>S $4.99</div><div class="row">Lettuce, Tomatoes, Cucumbers, Olives, Onions, &amp; Pepperoncini<span class="lead"></span>M $5.99</div><div class="row"><span class="lead"></span>L $6.99</div></div>
      <div class="item"><div class="row">Antipasto<span class="lead"></span>S $5.99</div><div>Ham, Salami, Lettuce, Tomatoes, Cucumbers,</div><div class="row">Olives, Onions, &amp; Pepperoncini. Topped with Mozzarella Cheese<span class="lead"></span>M $8.99</div><div class="row"><span class="lead"></span>L $11.99</div></div>
      <div class="item"><div>Bruiser Chicken Salad</div><div>Chicken, Parmesan Cheese, Lettuce, Tomatoes,</div><div class="row">Cucumbers, Olives, Onions, &amp; Pepperoncini<span class="lead"></span>S $6.99</div><div class="row"><span class="lead"></span>M $8.99</div><div class="row"><span class="lead"></span>L $11.99</div></div>
      <div class="item"><div>Caesar Salad</div><div>Romaine Lettuce, Parmesan Cheese, Croutons - Tossed in Caesar Dressing</div><div class="row"><span class="lead"></span>S $5.49</div><div class="row"><span class="lead"></span>M $6.99</div><div class="row"><span class="lead"></span>L $9.99</div></div>
      <div class="item"><div>Chicken Caesar Salad</div><div>Chicken, Romaine Lettuce, Parmesan Cheese, Croutons - Tossed in Caesar Dressing</div><div class="row"><span class="lead"></span>S $6.99</div><div class="row"><span class="lead"></span>M $8.99</div><div class="row"><span class="lead"></span>L $11.99</div></div>
      <div class="sub" style="margin-top:6px">Dressings: Ranch, Italian, Caesar, Blue Cheese, Balsamic, &amp; Vinaigrette.</div>
    </div>
  </div>
</section>

<!-- Inside spread -->
<section class="spread spread--inside">
  <div class="panel panel--black">
    <svg class="photo" style="top:240px;height:320px" width="308" height="320" role="img" aria-label="Photo of chicken wings with a cup of dipping sauce">
      <defs>
        <radialGradient id="wingsGlow" cx="45%" cy="55%" r="65%">
          <stop offset="0" stop-color="#7a5a3e"/>
          <stop offset=".6" stop-color="#3a2a20"/>
          <stop offset="1" stop-color="#141414"/>
        </radialGradient>
      </defs>
      <rect width="308" height="320" fill="url(#wingsGlow)"/>
    </svg>
    <div style="position:relative">
      <h2 class="accent">Appetizers &amp; Sides</h2>
      <div class="row">Mozzarella Sticks 6 Piece<span class="lead"></span>$7.99</div>
      <div class="row">Mozzarella Sticks 12 Piece<span class="lead"></span>$12.99</div>
      <div class="row">4 Piece Chicken Fingers Basket w/Fries<span class="lead"></span>$12.49</div>
      <div class="row">Fried Zucchini 12 Piece<span class="lead"></span>$9.99</div>
      <div class="row">Fried Zucchini 20 Piece<span class="lead"></span>$12.99</div>
      <div class="row">Fried Mushrooms 12 Piece<span class="lead"></span>$9.99</div>
      <div class="row">Fried Mushrooms 20 Piece<span class="lead"></span>$16.99</div>
      <div class="row">6 Piece Cheese Pizza Log<span class="lead"></span>$11.49</div>
      <div class="row">6 Piece Pepperoni &amp; Cheese Log<span class="lead"></span>$12.49</div>
      <div class="row">Garlic Knots 6 Piece<span class="lead"></span>$6.99</div>
      <div class="row">Garlic Knots 12 Piece<span class="lead"></span>$10.99</div>
      <div class="row">Garlic Knots 20 Piece<span class="lead"></span>$16.99</div>
      <div class="row">Garlic Bread<span class="lead"></span>$4.75</div>
      <div class="row">Garlic Bread w/Mozzarella<span class="lead"></span>$5.25</div>
      <div class="row">Garlic Bread w/Mozzarella<span class="lead"></span>$5.25</div>

      <h2 class="accent" style="margin-top:14px">Fries</h2>
      <div class="item"><div class="row">French Fries<span class="lead"></span>$4.75</div></div>
      <div class="item"><div>Queso Fries</div><div>They are what you think they are, fries smothered in Queso Cheese. $5.99</div></div>
      <div class="item"><div>Famous Philly Cheesesteak Fries</div><div class="row">French Fries Smothered W/Queso Cheese &amp; Philly Steak Meat<span class="lead"></span>$13.49</div></div>
      <div class="item"><div>Chicken Philly Cheese Fries</div><div class="row">French Fries Covered W/Queso Cheese and Philly Chicken Meat<span class="lead"></span>$13.49</div></div>

      <h2 class="accent" style="margin-top:8px">Wings</h2>
      <div class="item"><div>Bone-in Wings</div><div>Mild, Medium, Hot, Suicide, BBQ, Garlic Parmigiana,</div><div class="row">Spicy Asian, Lemon Pepper, Plain<span class="lead"></span>6 pc $8.99</div><div class="row"><span class="lead"></span>12 pc $16.99</div><div class="row"><span class="lead"></span>24 pc $29.99</div><div class="row"><span class="lead"></span>48 pc $56.99</div></div>
      <div class="item"><div>Boneless Wings</div><div>Mild, Medium, Hot, Suicide, BBQ, Garlic Parmigiana,</div><div class="row">Spicy Asian, Lemon Pepper, Plain<span class="lead"></span>6 pc $8.99</div><div class="row"><span class="lead"></span>12 pc $16.99</div><div class="row"><span class="lead"></span>24 pc $29.99</div></div>
      <h2 class="accent" style="margin-top:4px">Extras</h2>
      <div>Extra Dipping Sauce</div>
      <div class="row">Ranch, Blue Cheese, Mild, Medium, Hot, BBQ, Spicy Asian<span class="lead"></span>$.50</div>
    </div>
  </div>

  <div class="panel panel--red">
    <h2>Signature Pizzas</h2>
    <div class="item sizes"><div>Brooklyn Supreme</div><div>Pepperoni, Sausage, Mushroom, Green Peppers,</div><div class="row" style="margin-left:0">Onions, &amp; Extra Cheese<span class="lead"></span>14" M $23.95</div><div class="row"><span class="lead"></span>16" L $25.95</div><div class="row"><span class="lead"></span>18" XL $27.95</div></div>
    <div class="item sizes"><div>Bronx Meat Lovers</div><div class="row" style="margin-left:0">Pepperoni, Sausage, Ham, Bacon, &amp; Extra Cheese<span class="lead"></span>14" M $23.95</div><div class="row"><span class="lead"></span>16" L $25.95</div><div class="row"><span class="lead"></span>18" XL $27.95</div></div>
    <div class="item sizes"><div>Central Park Veggie</div><div>Mushrooms, Green Peppers, Onions, Black Olives, &amp; Extra Cheese</div><div class="row"><span class="lead"></span>14" M $21.95</div><div class="row"><span class="lead"></span>16" L $23.95</div><div class="row"><span class="lead"></span>18" XL $25.95</div></div>
    <div class="item sizes"><div>Buffalo Borough Chicken</div><div class="row" style="margin-left:0">Breaded Chicken in Hot Sauce Topped W/Ranch or Blue Cheese<span class="lead"></span>14" M $22.95</div><div class="row"><span class="lead"></span>16" L $24.95</div><div class="row"><span class="lead"></span>18" XL $26.95</div></div>
    <div class="item sizes"><div>Fifth Avenue Bacon Ranch</div><div class="row" style="margin-left:0">Breaded Chicken with Bacon and Ranch<span class="lead"></span>14" M $22.95</div><div class="row"><span class="lead"></span>16" L $24.95</div><div class="row"><span class="lead"></span>18" XL $26.95</div></div>
    <div class="item sizes"><div>Harlem BBQ Chicken</div><div class="row" style="margin-left:0">Breaded Chicken in BBQ Sauce<span class="lead"></span>14" M $22.95</div><div class="row"><span class="lead"></span>16" L $24.95</div><div class="row"><span class="lead"></span>18" XL $26.95</div></div>
    <div class="item sizes"><div>Little Italy Margarita</div><div class="row" style="margin-left:0">Fresh Mozzarella, Basil, &amp; Homemade Sauce<span class="lead"></span>14" M $21.95</div><div class="row"><span class="lead"></span>16" L $23.95</div><div class="row"><span class="lead"></span>18" XL $25.95</div></div>
    <div class="item sizes"><div>The Gil’s Chicken &amp; Jalapeño</div><div>Chicken, Jalapeño, &amp; Extra Cheese</div><div class="row" style="margin-left:0">OWNER’S FAVORITE<span class="lead"></span>14" M $22.95</div><div class="row"><span class="lead"></span>16" L $24.95</div><div class="row"><span class="lead"></span>18" XL $26.95</div></div>
    <div class="item sizes"><div>Broadway Bianca</div><div class="row" style="margin-left:0">Ricotta, Parmesan, &amp; Garlic - No Sauce<span class="lead"></span>14" M $21.95</div><div class="row"><span class="lead"></span>16" L $23.95</div><div class="row"><span class="lead"></span>18" XL $25.95</div></div>
    <div class="item sizes"><div>Broadway Bianca Deluxe</div><div class="row" style="margin-left:0">Ricotta, Mozzarella, Garlic, Spinach, &amp; Tomatoes<span class="lead"></span>14" M $22.95</div><div class="row"><span class="lead"></span>16" L $24.95</div><div class="row"><span class="lead"></span>18" XL $26.95</div></div>
    <h2 class="mixed" style="margin:6px 0 2px">Burgers</h2>
    <div>Single Smash Burger W/Cheese</div>
    <div class="row">1/3 LB Burger, Onions, Lettuce, Tomatoes, &amp; American Cheese<span class="lead"></span>$7.99</div>
    <div style="margin-top:4px">Double Smash Burger W/Cheese</div>
    <div class="row">Two 1/3 LB Burger, Onions, Lettuce, Tomatoes, &amp; American Cheese<span class="lead"></span>$9.99</div>
  </div>

  <div class="panel panel--black" style="padding-top:0">
    <svg class="photo" style="top:0;height:200px" width="308" height="200" role="img" aria-label="Photo of a pizza slice being lifted with stretching melted cheese">
      <defs>
        <radialGradient id="pizzaGlow" cx="65%" cy="45%" r="70%">
          <stop offset="0" stop-color="#e0a24a"/>
          <stop offset=".45" stop-color="#8a4a22"/>
          <stop offset="1" stop-color="#141414"/>
        </radialGradient>
      </defs>
      <rect width="308" height="200" fill="url(#pizzaGlow)"/>
    </svg>
    <div style="position:relative;padding-top:156px">
      <h2 class="accent">Build Your Own NY Pizza</h2>
      <div class="row" style="width:180px">Medium Cheese Pizza<span class="lead"></span>14" $15.50</div>
      <div class="row" style="width:180px">Large Cheese Pizza<span class="lead"></span>16" $16.50</div>
      <div class="row" style="width:180px">XL Cheese Pizza<span class="lead"></span>18" $18.50</div>
      <div class="item" style="margin-top:8px"><div>Whole Pie Toppings</div><div>$3.99 each: Anchovies • Banana Peppers • Black Olives • Green Olives • Extra Cheese • Extra Sauce • Garlic • Green Peppers • Ham • Jalapeños • Meatballs • Mushrooms • Onions • Pepperoni • Pineapple • Salami • Sausage • Spinach • Tomatoes • Bacon • Broccoli<br>$4.99 each: Artichokes • Bacon • Chicken • Eggplant • Green Olives • Meatball • Ricotta</div></div>
      <div class="item"><div>Half Pie Toppings</div><div>$2.00 each: Anchovies • Banana Peppers • Black Olives • Green Olives • Extra Cheese • Extra Sauce • Garlic • Green Peppers • Ham • Jalapeños • Meatballs • Mushrooms • Onions • Pepperoni • Pineapple • Salami • Sausage • Spinach • Tomatoes • Bacon • Broccoli<br>$2.50 each: Artichokes • Bacon • Chicken • Eggplant • Green Olives • Meatball • Ricotta</div></div>
      <div class="item"><div>SUBS</div><div>Vitale Chicken Sub</div><div>Marinated &amp; Cubed Chicken W/ Sauteed Mushrooms, Jalapeños, Bacon, Ranch, Topped W/Melted Pepper Jack, Swiss, Provolone, American, &amp; Parmesan Cheese on</div><div class="row">an Rosetti Roll<span class="lead"></span>$12.49</div></div>
      <div class="item"><div>Famous Philly Cheesesteak</div><div>Sliced Steak, Onions, &amp; American Cheese on an Rosetti Roll. Make it a Hogie</div><div class="row">(Lettuce &amp; Tomato) for $1.00<span class="lead"></span>$12.49</div></div>
      <div class="item"><div>Chicken Philly Cheesesteak</div><div>Sliced Chicken, Onions, &amp; American Cheese on an Rosetti Roll. Make it Hogie</div><div class="row">style for an extra $1.00<span class="lead"></span>$12.49</div><div>Mama’s Meatball Sub</div><div>Homemade meatballs with ground turkey &amp; Italian sausage, smothered in</div><div class="row">marinara and finished off with Provolone Cheese on an Rosetti Roll<span class="lead"></span>$12.49</div></div>
      <div>Popular Philly add-ons include: $.50 - mushrooms, onions, green peppers, jalapeños, banana peppers, black olives, tomatoes, lettuce, marinara, bacon, pepperoni, queso, pepper jack, and provolone<br>$3.00 – Extra Meat</div>
    </div>
  </div>
</section>

</body>
</html>
```